Boutique town planning business needs a Business Card design

We need a business card design for a new company called The Zoning Bridgeway. We provide town planning and urban design services to government, business and community groups. We would like to see the designs use the colours in the logo (blue, deep red, green and amber), plenty of white and including black and grey in the writing. The final design should communicate collaboration, creativity and professionalism and that we are approachable.

Industry/Entity Type

Town

```html
<!DOCTYPE html>
<html lang="en">
<head>
<meta charset="utf-8">
<title>The Zoning Bridgeway – Business Card</title>
<link rel="stylesheet" href="https://fonts.googleapis.com/css2?family=Ubuntu:wght@400;500;700&display=swap">
<style>
  :root {
    --page-bg: #e9e6e1;
    --card-white: #ffffff;
    --card-shade: #eeeeee;
    --brand-red: #9b3327;
    --brand-green: #79a92f;
    --brand-blue: #4f86b3;
    --brand-amber: #e1921f;
    --ink-black: #1b1b1b;
    --ink-grey: #5f6368;
  }
  * { box-sizing: border-box; margin: 0; padding: 0; }
  html, body {
    width: 1200px; height: 1200px; overflow: hidden;
    background: var(--page-bg);
    font-family: "Ubuntu", sans-serif;
  }
  .canvas { position: relative; width: 1200px; height: 1200px; }

  .card {
    position: absolute; left: 150px;
    width: 900px; height: 514px;
    background: linear-gradient(160deg, var(--card-white) 55%, var(--card-shade) 100%);
    box-shadow: 0 10px 30px rgba(0,0,0,.18);
    overflow: hidden;
  }
  .card--front { top: 60px; }
  .card--back  { top: 626px; }

  /* front */
  .front-swoosh { position: absolute; inset: 0; width: 100%; height: 100%; }
  .brand-block { position: absolute; left: 70px; top: 60px; }
  .brand-dot {
    width: 110px; height: 110px; border-radius: 50%;
    background: var(--brand-blue);
  }
  .brand-name {
    margin-top: 18px;
    font-size: 28px; font-weight: 700; color: var(--ink-grey);
    white-space: nowrap;
  }
  .person { position: absolute; left: 440px; top: 40px; }
  .person__name { font-size: 40px; font-weight: 400; color: var(--brand-red); }
  .person__role { margin-top: 8px; font-size: 28px; color: var(--ink-black); }

  .contact-list { position: absolute; list-style: none; }
  .contact-list--online { left: 440px; top: 218px; }
  .contact-list--office { left: 70px; top: 300px; }
  .contact-list li {
    display: flex; align-items: center; gap: 12px;
    font-size: 21px; color: var(--ink-black);
    margin-bottom: 22px; white-space: nowrap;
  }
  .contact-icon { width: 20px; height: 20px; flex: none; fill: var(--ink-black); }

  /* back */
  .back-layout {
    position: absolute; inset: 0;
    display: flex; flex-direction: column; align-items: center; justify-content: center;
    gap: 34px;
  }
  .back-dot {
    width: 220px; height: 220px; border-radius: 50%;
    background: var(--brand-red);
  }
  .back-name {
    font-size: 68px; font-weight: 700; color: var(--ink-grey);
    white-space: nowrap;
  }
</style>
</head>
<body>
<main class="canvas">

  <section class="card card--front" aria-label="Business card front">
    <svg class="front-swoosh" viewBox="0 0 900 514" preserveAspectRatio="none" aria-hidden="true">
      <path d="M0,440 C250,418 520,470 900,300 L900,514 L0,514 Z" fill="var(--brand-red)"/>
      <path d="M300,445 C540,425 740,360 900,248 L900,272 C740,382 540,442 300,445 Z" fill="var(--brand-green)"/>
    </svg>

    <div class="brand-block">
      <div class="brand-dot"></div>
      <p class="brand-name">The Zoning Bridgeway</p>
    </div>

    <div class="person">
      <p class="person__name">Marisa Holloway</p>
      <p class="person__role">Director</p>
    </div>

    <ul class="contact-list contact-list--online">
      <li>
        <svg class="contact-icon" viewBox="0 0 20 20" aria-hidden="true"><path d="M1 4h18v12H1z" fill="none" stroke="currentColor"/><path d="M1 4h18v12H1zM2 5.5v.4l8 5.6 8-5.6v-.4z" /></svg>
        hello@thezoningbridgeway.com.au
      </li>
      <li>
        <svg class="contact-icon" viewBox="0 0 20 20" aria-hidden="true"><g fill="none" stroke="#1b1b1b" stroke-width="1.6"><circle cx="10" cy="10" r="8"/><ellipse cx="10" cy="10" rx="3.5" ry="8"/><path d="M2 10h16M3.5 6h13M3.5 14h13"/></g></svg>
        www.thezoningbridgeway.com.au
      </li>
    </ul>

    <ul class="contact-list contact-list--office">
      <li>
        <svg class="contact-icon" viewBox="0 0 20 20" aria-hidden="true"><path d="M4 1.5l3.2 3.6-1.6 2.4c1 2.4 2.6 4 5 5l2.4-1.6 3.6 3.2-2 3.2C8 16.6 3.4 12 1 4.6z"/></svg>
        ABN 51824096317
      </li>
      <li>
        <svg class="contact-icon" viewBox="0 0 20 20" aria-hidden="true"><path d="M4 1.5l3.2 3.6-1.6 2.4c1 2.4 2.6 4 5 5l2.4-1.6 3.6 3.2-2 3.2C8 16.6 3.4 12 1 4.6z"/></svg>
        0412 555 038
      </li>
    </ul>
  </section>

  <section class="card card--back" aria-label="Business card back">
    <div class="back-layout">
      <div class="back-dot"></div>
      <p class="back-name">The Zoning Bridgeway</p>
    </div>
  </section>

</main>
</body>
</html>
```